Lofty Intake needs a 8.5" X 11" flyer to give to college presidents

We need a flyer design for Lofty Intake that briefly explains what we do and encourages college presidents to give the flyer to their directors of admission. Please be consistent with our brand www.loftyintake.example. I've attached an example of a cool three dimensional flyer that I like...but I'm open to all ideas.

FRONT: The first on-line and fully automated recruiting tool that allows admissions officers to electronically contact high school seniors and send them invitations to apply that include estimates of merit aid.

BACK: Lofty Intake brings your college or university students' mobile devices and desktops. Knowing their credentials, admissions offers can send either a single student or groups of students invitations to apply that include offers of merit aid. Your school’s invitation is a recruiting document that appeals to students and parents with a clear price signal, and to students and counselors with customizable links to your college or universities website, rankings, social media and any particular information or commendation.

For information about how Lofty Intake fits into your enrollment strategy and expands your access to students, families and counselors, please contact us by phone 866.519.2274 or email admin@loftyintake.example. An on-line presentation of Lofty Intake takes less than 30 minutes.

college presidents and admissions officers

Education

• front and back designs
• a look of depth or three dimensions

```html
<!DOCTYPE html>
<html lang="en">
<head>
<meta charset="utf-8">
<title>Lofty Intake Flyer – Front and Back</title>
<link rel="stylesheet" href="https://fonts.googleapis.com/css2?family=Merriweather:wght@700;900&family=Open+Sans:wght@400;600&family=Courgette&family=Tinos&display=swap">
<style>
  :root {
    --canvas: #d6d7d9;
    --frame-dark: #2b2c2e;
    --frame-darker: #1d1e20;
    --panel-light: #eceef0;
    --panel-mid: #cfd3d7;
    --slab-top: #c3c7cc;
    --slab-bottom: #8f949a;
    --slab-edge: #6d7277;
    --navy: #1d3557;
    --ink: #1f2c44;
    --red: #b3242c;
    --red-dark: #8c1a21;
    --midnight: #0f1a27;
    --midnight-2: #1c2a39;
    --blue-band: #1d4c78;
    --white: #ffffff;
    --muted: #c9ccd0;
  }
  * { box-sizing: border-box; margin: 0; padding: 0; }
  html, body { width: 1200px; height: 800px; overflow: hidden; }
  body { background: var(--canvas); position: relative; font-family: "Open Sans", sans-serif; }

  .flyer {
    position: absolute; top: 100px; width: 420px; height: 600px;
    box-shadow: 0 14px 30px rgba(0,0,0,.35);
    overflow: hidden;
  }
  .flyer--front { left: 140px; background: var(--frame-dark); padding: 18px; }
  .flyer--back { left: 640px; background: linear-gradient(var(--midnight), var(--midnight-2)); }

  /* FRONT */
  .brand-panel {
    height: 170px;
    background: linear-gradient(var(--panel-light), var(--panel-mid));
    box-shadow: inset 0 -10px 0 #b4b9be, inset 10px 0 0 #dfe2e5, inset -10px 0 0 #b9bdc2;
    display: flex; align-items: center; justify-content: center; gap: 12px;
  }
  .brand-mark { width: 22px; height: 22px; background: var(--red); }
  .brand-name {
    font-family: "Merriweather", serif; font-weight: 900; font-size: 40px;
    color: var(--navy); letter-spacing: .5px;
  }
  .pitch { list-style: none; margin-top: 10px; }
  .pitch__slab {
    height: 44px; margin: 0 4px 6px;
    background: linear-gradient(var(--slab-top), var(--slab-bottom));
    border-top: 2px solid #e2e5e8; border-bottom: 5px solid var(--slab-edge);
    box-shadow: 0 4px 6px rgba(0,0,0,.45);
    display: flex; align-items: center; justify-content: center;
    font-family: "Merriweather", serif; font-weight: 700; font-size: 18px;
    color: var(--ink);
  }
  .pitch__slab:nth-child(odd) { margin-left: 14px; margin-right: 0; }
  .front-base { height: 46px; background: var(--frame-darker); margin: 4px -18px 0; }

  /* BACK */
  .back-wave { position: absolute; top: 0; left: 0; width: 420px; height: 330px; }
  .back-intro {
    position: absolute; top: 46px; left: 30px; right: 30px;
    color: var(--white); font-size: 13.2px; line-height: 1.5; text-align: center;
  }
  .back-cta {
    position: absolute; top: 348px; left: 30px; right: 30px;
    color: var(--white); font-size: 16px; line-height: 1.4; text-align: center;
  }
  .contact-band {
    position: absolute; top: 440px; left: 0; right: 0; height: 58px;
    background: linear-gradient(#24598a, var(--blue-band));
    display: flex; align-items: center; justify-content: center;
    font-family: "Courgette", cursive; font-size: 30px; color: var(--white);
  }
  .contact-rule { position: absolute; top: 498px; left: 0; right: 0; height: 8px; background: var(--red); }
  .contact-bar {
    position: absolute; top: 506px; left: 0; right: 0; height: 94px;
    background: #2a2b2d; padding-top: 14px;
    font-family: "Tinos", serif; color: var(--white);
  }
  .contact-list { display: flex; justify-content: center; gap: 22px; font-size: 16px; list-style: none; }
  .contact-list li { display: flex; align-items: center; gap: 6px; }
  .contact-list svg { width: 16px; height: 16px; fill: var(--white); }
  .contact-note { margin-top: 14px; text-align: center; font-size: 11px; color: var(--muted); }
  .contact-note strong { color: var(--white); font-size: 13px; }
</style>
</head>
<body>
  <section class="flyer flyer--front" aria-label="Flyer front">
    <header class="brand-panel">
      <span class="brand-mark"></span>
      <span class="brand-name">Lofty Intake</span>
    </header>
    <ul class="pitch">
      <li class="pitch__slab">The first on-line and fully</li>
      <li class="pitch__slab">automated recruiting tool that</li>
      <li class="pitch__slab">allows admissions officers to</li>
      <li class="pitch__slab">electronically contact high</li>
      <li class="pitch__slab">school seniors and send them</li>
      <li class="pitch__slab">invitations to apply that</li>
      <li class="pitch__slab">include estimates of merit aid.</li>
    </ul>
    <div class="front-base"></div>
  </section>

  <section class="flyer flyer--back" aria-label="Flyer back">
    <svg class="back-wave" viewBox="0 0 420 330" preserveAspectRatio="none" aria-hidden="true">
      <defs>
        <linearGradient id="redFade" x1="0" y1="0" x2="0" y2="1">
          <stop offset="0" stop-color="#8c1a21"/>
          <stop offset=".35" stop-color="#b3242c"/>
          <stop offset="1" stop-color="#a01f27"/>
        </linearGradient>
      </defs>
      <path d="M0 0H420V300Q210 350 0 300Z" fill="url(#redFade)"/>
    </svg>
    <p class="back-intro">Lofty Intake brings your college or university students' mobile devices and desktops. Knowing their credentials, admissions offers can send either a single student or groups of students invitations to apply that include offers of merit aid. Your school's invitation is a recruiting document that appeals to students and parents with a clear price signal, and to students and counselors with customizable links to your college or universities website, rankings, social media and any particular information or commendation.</p>
    <p class="back-cta">For information about how Lofty Intake fits into your enrollment strategy and expands your access to students, families and counselors,</p>
    <div class="contact-band">Please contact us by</div>
    <div class="contact-rule"></div>
    <footer class="contact-bar">
      <ul class="contact-list">
        <li><svg viewBox="0 0 24 24" aria-hidden="true"><path d="M6.6 10.8a15 15 0 0 0 6.6 6.6l2.2-2.2a1 1 0 0 1 1-.25 11.4 11.4 0 0 0 3.6.57 1 1 0 0 1 1 1V20a1 1 0 0 1-1 1A17 17 0 0 1 3 4a1 1 0 0 1 1-1h3.5a1 1 0 0 1 1 1c0 1.25.2 2.45.57 3.57a1 1 0 0 1-.25 1z"/></svg>866.519.2274</li>
        <li><svg viewBox="0 0 24 24" aria-hidden="true"><path d="M2 5h20v14H2zm2 2v.4l8 5.1 8-5.1V7zm0 2.8V17h16V9.8l-8 5.1z"/></svg>admin@loftyintake.example</li>
      </ul>
      <p class="contact-note">An on-line presentation of Lofty Intake takes less than <strong>30</strong> minutes.</p>
    </footer>
  </section>
</body>
</html>
```